Lumora vale- referral cards for new customers

Hey,

I would like 1 set of business cards with the following details:

10% off any sales / coupon code
Our phone number: 4702938165
Menu :Lumoravale.example (for the menu)
A line left blank to hand write an activation code: either on top or just on one side

Include the Lumora Vale logo ( your choice of black or white logo)
This card is to drive orders for people to order a cannabis order with Lumora Vale. Please make the logo a large part of the card on both sides.

Target Market(s)

People who consume cannabis 21 and up

Industry/Entity Type

Business

Contact Information for Business Card

This business card will be given to customers so they can then give it to other customers and generate referalls. We need this card to be elegant, impressionable, professional, and something worth keeping and passing to friends.

Font styles to use
Decorative
Script

Colors
33a6d7
85acd3
3176b5
0455a3
0592cd
85cae6
cee9f5
eaf1f7
757575

Requirements
Must have
• Our website
• Phone Number
• The 10% off an order
• Spot for activation code
Nice to have
• Eye catching design
• Look classy
• Textured feel or textured look
Should not have
• Do not look super cannabis heady
• Do not look attractive to children

```html
<!DOCTYPE html>
<html lang="en">
<head>
<meta charset="utf-8">
<title>Lumora Vale – Referral Card</title>
<link rel="stylesheet" href="https://fonts.googleapis.com/css2?family=Merriweather:wght@400;700&display=swap">
<style>
  :root {
    --backdrop: #3b3b3b;
    --front-light: #85cae6;
    --front-mid: #33a6d7;
    --front-deep: #3176b5;
    --front-edge: #0455a3;
    --band: #cee9f5;
    --band-edge: #b7d9e8;
    --paper: #ffffff;
    --ink: #2b2b2b;
    --ink-soft: #333333;
    --accent: #0592cd;
    --frame: #bdbdbd;
    --grey: #757575;
  }
  * { box-sizing: border-box; margin: 0; padding: 0; }
  html, body { width: 1097px; height: 1200px; overflow: hidden; }
  body {
    position: relative;
    background: var(--backdrop);
    font-family: "Merriweather", Georgia, serif;
    color: var(--ink);
  }
  .card {
    position: absolute;
    left: 221px;
    width: 656px;
    border-radius: 22px;
    overflow: hidden;
  }
  .card--front {
    top: 157px;
    height: 385px;
    background:
      radial-gradient(ellipse at 58% 30%, rgba(133,202,230,0.55), transparent 60%),
      linear-gradient(135deg, var(--front-deep) 0%, var(--front-mid) 45%, var(--front-light) 70%, var(--front-deep) 100%);
  }
  .card--front::after {
    content: "";
    position: absolute; inset: 0;
    box-shadow: inset 0 0 60px rgba(4,85,163,0.55);
    border-radius: 22px;
  }
  .front-mark {
    position: absolute;
    left: 50%; top: 75px;
    width: 200px; height: 200px;
    margin-left: -100px;
    border-radius: 50%;
    background: radial-gradient(circle, #9fd3e6 0%, #4f6b4a 70%, #2f4a33 100%);
  }
  .front-name {
    position: absolute;
    left: 0; right: 0; top: 292px;
    text-align: center;
    font-size: 38px;
    font-weight: 400;
    letter-spacing: 1px;
    color: var(--ink);
  }
  .card--back {
    top: 607px;
    height: 384px;
    background: var(--paper);
  }
  .band {
    position: absolute; left: 0; right: 0; height: 34px;
    background: linear-gradient(90deg, var(--band-edge), var(--band), var(--band-edge));
  }
  .band--top { top: 0; }
  .band--bottom { bottom: 0; }
  .logo-tile {
    position: absolute;
    left: 59px; top: 71px;
    width: 213px; height: 239px;
    border: 2px solid var(--frame);
    border-radius: 16px;
    background: var(--paper);
    box-shadow: 14px 10px 28px rgba(0,0,0,0.35);
  }
  .logo-tile__mark {
    position: absolute;
    left: 50%; top: 20px;
    width: 150px; height: 150px;
    margin-left: -75px;
    border-radius: 50%;
    background: radial-gradient(circle, #9fd3e6 0%, #4f6b4a 70%, #2f4a33 100%);
  }
  .logo-tile__name {
    position: absolute;
    left: 0; right: 0; top: 188px;
    text-align: center;
    font-size: 24px;
    color: var(--ink);
  }
  .details {
    position: absolute;
    left: 384px; top: 50px;
    font-size: 21px;
    color: var(--ink-soft);
    letter-spacing: 0.5px;
  }
  .details__row {
    position: absolute;
    left: 0;
    white-space: nowrap;
    display: flex;
    align-items: center;
  }
  .details__row b { font-weight: 700; }
  .icon {
    width: 22px; height: 22px;
    margin-left: -38px; margin-right: 16px;
    flex: none;
  }
  .offer { left: 39px; top: 0; }
  .activation { top: 42px; }
  .phone { top: 209px; }
  .web { top: 256px; }
</style>
</head>
<body>
  <section class="card card--front">
    <div class="front-mark" role="img" aria-label="Round brand emblem area"></div>
    <p class="front-name">Lumora Vale</p>
  </section>

  <section class="card card--back">
    <div class="band band--top"></div>
    <div class="band band--bottom"></div>

    <div class="logo-tile">
      <div class="logo-tile__mark" role="img" aria-label="Round brand emblem area"></div>
      <p class="logo-tile__name">Lumora Vale</p>
    </div>

    <div class="details">
      <p class="details__row offer"><b>10%</b>&nbsp;off any sales</p>
      <p class="details__row activation" style="left:39px">
        <svg class="icon" viewBox="0 0 22 22" aria-hidden="true"><circle cx="11" cy="11" r="9" fill="var(--accent)"/></svg>
        activation code
      </p>
      <p class="details__row phone" style="left:39px">
        <svg class="icon" viewBox="0 0 22 22" aria-hidden="true">
          <path d="M2 9 Q11 2 20 9 L18 12 L15 10 L15 8 Q11 6 7 8 L7 10 L4 12 Z" fill="var(--accent)"/>
          <rect x="5" y="12" width="12" height="7" rx="1.5" fill="var(--accent)"/>
        </svg>
        4702938165
      </p>
      <p class="details__row web" style="left:39px">
        <svg class="icon" viewBox="0 0 22 22" aria-hidden="true" fill="none" stroke="var(--accent)" stroke-width="1.6">
          <circle cx="11" cy="11" r="9" fill="var(--accent)" fill-opacity="0.25"/>
          <ellipse cx="11" cy="11" rx="4" ry="9"/>
          <line x1="2" y1="11" x2="20" y2="11"/>
          <line x1="4" y1="6" x2="18" y2="6"/>
          <line x1="4" y1="16" x2="18" y2="16"/>
        </svg>
        Lumoravale.example
      </p>
    </div>
  </section>
</body>
</html>
```